packaging design for disposable trash bag

We need 3 design for 3 of our products. first item is trash bag,the second item is disposable table cover and third is food packaging bag . We are a company in Singapore selling disposable product. This packaging products will be sold on shelf or online.

Attached is the requirement of the product. And some samples.
Updates

Target Market(s)

adult, most likely housewife

Requirements
Must have
• Packing design requirement for trash bag
• 1. Include company logo design, which is attached in the creative brief. MIRVALE POLYPAK.
• 2. Clear showing of the product and its illustration of using. Eg. The trash bin.
• 3. Allocate a box for the purpose of sticking product size sticker.
• 4. Each packing bag holds 10pcs
• 5. Show of country of origin. Product of Singapore.
• 6. Use of one colour for printing of packing bag ( Black / blue/ bright Green/ white )
• 7. Show of warning: Keep polythene bags away from young children
• 8. dimension of the packagaing printing area : Lenght : 20 cm , Height 26 cm
• Packing design requirement for disposable Table Cover
• 1. Include company logo design, which is attached in the creative brief. Our company is MIRVALE POLYPAK.
• 2. Clear showing of the product and its illustration of using. Eg. The table?.
• 4. Each packing bag holds 5pcs
• 6. Use of one colour for printing of the packing bag ( Black / blue/ bright Green )
• Packing design requirement for disposable food packaging plastic bag
• 2. Clear showing of the product and its illustration of using. Eg. Food?.
• 4. Show of country of origin. Product of Singapore.
• 5. Use of one colour for printing of the packing bag ( Black/ bright green )
• 6. Show of warning: Keep polythene bags away from young children
• 7. Show of product information: hygienic, food grade, freezer resistance, grease proof, damp proof, heat resistant.
• 8. Include the open here packing opening.
• 9. dimension of the packagaing printing area : Lenght : 15 cm , Height 22 cm
Nice to have
• requirement is stated in the must have. Good to allocate some space beside the packaging PCS area for promotion stickers . And also space allocated for bar code stickers.
Should not have
• no more than one color for printing

```html
<!DOCTYPE html>
<html lang="en">
<head>
<meta charset="utf-8">
<title>Mirvale Polypak – Disposable Food Packaging Plastic Bag</title>
<link rel="stylesheet" href="https://fonts.googleapis.com/css2?family=Anton&family=Archivo+Black&family=Arimo:wght@400;700&family=Roboto+Condensed:wght@500&display=swap">
<style>
  :root {
    --ink: #111114;
    --film: #cdd1dd;
    --film-shade: #b9bece;
  }
  html, body {
    margin: 0;
    padding: 0;
    width: 1200px;
    height: 766px;
    overflow: hidden;
    background: var(--film);
  }
  .pack {
    position: relative;
    width: 1200px;
    height: 766px;
    color: var(--ink);
    font-family: "Arimo", Arial, sans-serif;
  }
  .pack-lines {
    position: absolute;
    left: 0;
    top: 0;
  }
  .label {
    position: absolute;
    margin: 0;
    white-space: nowrap;
    transform: translate(-50%, -50%);
  }
  .size-title {
    font-family: "Archivo Black", sans-serif;
    font-size: 13px;
    letter-spacing: 1px;
    background: var(--film);
    padding: 0 5px;
  }
  .size-note { font-size: 15px; }
  .open-note { font-size: 14px; font-weight: 700; }
  .suitable {
    font-size: 11px;
    font-weight: 700;
    text-align: center;
    line-height: 15px;
  }
  .features {
    position: absolute;
    left: 196px;
    top: 281px;
    margin: 0;
    padding: 0;
    list-style: none;
    font-family: "Archivo Black", sans-serif;
    font-size: 19px;
    line-height: 29.4px;
    white-space: nowrap;
    transform: scaleX(0.88);
    transform-origin: left top;
  }
  .features li::before {
    content: "";
    display: inline-block;
    width: 0;
    height: 0;
    border-top: 7px solid transparent;
    border-bottom: 7px solid transparent;
    border-left: 8px solid var(--ink);
    margin-right: 4px;
    vertical-align: -1px;
  }
  .food-art {
    position: absolute;
    left: 804px;
    top: 320px;
    width: 196px;
    height: 54px;
    border-radius: 10px;
    background: linear-gradient(90deg, #8a8e99, #2a2b30);
  }
  .brand-mark {
    position: absolute;
    left: 300px;
    top: 492px;
    width: 52px;
    height: 52px;
    background: var(--ink);
  }
  .brand-name { font-size: 25px; }
  .brand-suffix { font-size: 25px; }
  .brand-web { font-size: 16px; font-weight: 700; }
  .disposal {
    font-family: "Roboto Condensed", sans-serif;
    font-size: 14px;
    text-align: center;
    line-height: 19px;
    transform: translate(-50%, -50%) scaleX(0.85);
  }
  .origin { font-size: 17px; }
  .barcode-note { font-size: 15px; font-weight: 700; }
</style>
</head>
<body>
<main class="pack">
  <svg class="pack-lines" width="1200" height="766" viewBox="0 0 1200 766">
    <g fill="none" stroke="var(--ink)">
      <rect x="179" y="95" width="843" height="574" rx="12" stroke-width="3"/>
      <line x1="179" y1="264" x2="1022" y2="264" stroke-width="2.5"/>
      <line x1="466" y1="95" x2="466" y2="264" stroke-width="2.5"/>
      <rect x="181" y="112" width="285" height="152" stroke-width="2"/>
      <line x1="179" y1="468" x2="474" y2="468" stroke-width="2.5"/>
      <line x1="726" y1="468" x2="1022" y2="468" stroke-width="2.5"/>
      <line x1="179" y1="646" x2="1022" y2="646" stroke-width="2.5"/>
      <g class="sticker-corners" stroke-width="2.5">
        <polyline points="186,148 186,128 210,128"/>
        <polyline points="435,128 459,128 459,148"/>
        <polyline points="186,233 186,253 210,253"/>
        <polyline points="435,253 459,253 459,233"/>
      </g>
      <g class="sticker-corners" stroke-width="2.5">
        <polyline points="755,532 755,509 780,509"/>
        <polyline points="967,509 992,509 992,532"/>
        <polyline points="755,606 755,629 780,629"/>
        <polyline points="967,629 992,629 992,606"/>
      </g>
      <ellipse cx="599" cy="378" rx="187" ry="92" stroke-width="3.5"/>
      <ellipse cx="599" cy="378" rx="177" ry="83" stroke-width="1.5" stroke-dasharray="9 4"/>
      <polyline points="514,361 499,378 514,395" stroke-width="4"/>
      <polyline points="683,361 698,378 683,395" stroke-width="4"/>
    </g>

    <text x="1002" y="154" text-anchor="end" font-family="Anton, sans-serif" font-size="42" fill="var(--ink)" textLength="214" lengthAdjust="spacingAndGlyphs">DISPOSABLE</text>
    <text x="484" y="252" font-family="Anton, sans-serif" font-size="104" fill="var(--ink)" textLength="518" lengthAdjust="spacingAndGlyphs">FOOD PACKAGING PLASTIC BAG</text>

    <g class="usage-badges" fill="var(--ink)">
      <path d="M532 589 l18 30 h-36 z" fill="none" stroke="var(--ink)" stroke-width="3"/>
      <rect x="565" y="592" width="32" height="30" rx="3" fill="none" stroke="var(--ink)" stroke-width="3"/>
      <circle cx="630" cy="607" r="18"/>
      <rect x="658" y="590" width="32" height="32" rx="3" fill="none" stroke="var(--ink)" stroke-width="3"/>
    </g>

    <text x="206" y="664" font-family="Archivo Black, sans-serif" font-size="15" fill="var(--ink)" textLength="788" lengthAdjust="spacingAndGlyphs">WARNING: PLEASE KEEP POLYTHENE BAGS AWAY FROM YOUNG CHILDREN</text>
  </svg>

  <p class="label size-title" style="left:322px; top:113px;">SIZE</p>
  <p class="label size-note" style="left:322px; top:190px;">SIZE (DIMENSION)</p>

  <ul class="features">
    <li>HYGENIC</li>
    <li>FOOD GRADE</li>
    <li>GREASE PROOF</li>
    <li>DAMP PROOF</li>
    <li>FREEZER RESISTANT</li>
    <li>HEAT RESISTANT</li>
  </ul>

  <p class="label open-note" style="left:599px; top:378px;">OPEN HERE</p>

  <div class="food-art" role="img" aria-label="Illustration of sandwich, roast chicken, steak and fruit"></div>
  <p class="label suitable" style="left:902px; top:411px;">SUITABLE FOR<br>MOST FOOD PACKAGING</p>

  <div class="brand-mark" aria-hidden="true"></div>
  <p class="label brand-name" style="left:326px; top:573px;">MIRVALE POLYPAK</p>
  <p class="label brand-suffix" style="left:326px; top:598px;">PTE LTD</p>
  <p class="label brand-web" style="left:326px; top:620px;">www.mirvalepolypak.com</p>

  <p class="label disposal" style="left:599px; top:535px;">USED BAGS SHOULD BE DISPOSED OF IN A PROPER<br>MANNER TO ENSURE CLEANLINESS TO THE<br>SURROUNDING ENVIRONMENT.</p>

  <p class="label origin" style="left:872px; top:495px;">PRODUCT OF SINGAPORE</p>
  <p class="label barcode-note" style="left:872px; top:569px;">BARCODE</p>
</main>
</body>
</html>
```